Inspirational speaker and coach Corinne Valbeck is building a website

Design, Create and launch a 10-15 page Wordpress website. Please research Corinne online and use examples you have access to.

```html
<!DOCTYPE html>
<html lang="en">
<head>
<meta charset="utf-8">
<title>Corinne Valbeck — Helping Create Success</title>
<link rel="stylesheet" href="https://fonts.googleapis.com/css2?family=DM+Serif+Display&family=Rubik:wght@400;500;700&family=Work+Sans:wght@400;500;600;700&display=swap">
<style>
:root{
  --gold:#d4ad3f;
  --ink:#252b36;
  --ink-deep:#1d222b;
  --text:#2b2f36;
  --muted:#5e636b;
  --ghost:#e9e9ec;
  --panel:#f2f2f3;
  --white:#ffffff;
}
*{box-sizing:border-box;margin:0;padding:0}
html,body{width:1200px;height:4345px;overflow:hidden}
body{position:relative;background:var(--white);font-family:"Work Sans",sans-serif;color:var(--text)}
.abs{position:absolute}
a{color:inherit;text-decoration:none}

/* top bar */
.topbar{left:0;top:0;width:1200px;height:41px;background:var(--ink);color:var(--white);font-size:12px;font-weight:500}
.topbar .tagline{left:60px;top:13px}
.topbar .phone{left:696px;top:13px}
.topbar .mailbox{left:830px;top:0;width:185px;height:41px;background:#2e3542;padding:13px 0 0 14px}
.topbar .socials{left:1036px;top:14px;display:flex;gap:17px}
.topbar .socials span{width:12px;height:12px;background:#cfd2d8;border-radius:2px;display:block}

/* nav */
.nav{left:0;top:41px;width:1200px;height:70px;background:var(--white)}
.brand{font-family:"Rubik",sans-serif;font-weight:700}
.nav .brand{left:60px;top:22px;font-size:22px;color:var(--ink)}
.nav .menu{left:366px;top:28px;display:flex;gap:28px;font-size:12.5px;font-weight:500;color:var(--ink)}
.nav .menu .active{color:var(--gold)}
.nav .cta{left:964px;top:14px;width:176px;height:44px;border:1.5px solid var(--gold);color:var(--gold);font-size:12px;font-weight:600;letter-spacing:.8px;text-align:center;line-height:41px}

/* hero */
.hero{left:0;top:111px;width:1200px;height:507px;background:var(--ink);overflow:hidden}
.hero .photo{left:506px;top:18px;width:405px;height:489px;background:radial-gradient(ellipse at 50% 40%,#9a9a9c 0%,#5b5c60 55%,#30343c 100%);border-radius:180px 180px 0 0}
.hero h1{left:157px;top:100px;font-family:"DM Serif Display",serif;font-weight:400;font-size:60px;line-height:62px;color:var(--white)}
.hero p{left:157px;top:246px;width:400px;font-family:"DM Serif Display",serif;font-size:13.5px;line-height:23px;color:#e6e7ea}
.btn{display:block;background:var(--gold);color:var(--white);font-size:13px;font-weight:600;text-align:center;line-height:41px}
.hero .btn{left:157px;top:348px;width:140px;height:41px}
.hero .feature{display:flex;gap:18px;align-items:flex-start}
.hero .blog{left:844px;top:117px;width:295px;height:118px;background:#f1f1f2;border-radius:6px;padding:24px 20px}
.hero .videos{left:861px;top:292px;width:290px}
.feature .ico{flex:none;width:56px;height:56px;border-radius:50%;background:var(--gold);display:flex;align-items:center;justify-content:center}
.videos .ico{background:#f1f1f2}
.feature h3{font-family:"Rubik",sans-serif;font-weight:500;font-size:17px;margin:3px 0 8px}
.feature em{font-size:12px;line-height:18px;display:block}
.blog h3,.blog em{color:var(--ink)}
.videos h3,.videos em{color:var(--white)}

/* section heading with ghost word */
.ghost{font-family:"DM Serif Display",serif;font-size:66px;color:var(--ghost);line-height:1}
.sec-title{font-family:"Rubik",sans-serif;font-weight:400;font-size:35px;color:var(--ink);line-height:42px}
.center{left:0;width:1200px;text-align:center}
.copy{font-size:12.5px;line-height:23px;color:var(--muted)}

/* device frame */
.tablet{background:#2a2d33;border-radius:12px;padding:22px 18px}
.tablet .screen{width:100%;height:100%;border-radius:2px}
.playmark{left:50%;top:50%;width:44px;height:44px;margin:-22px 0 0 -22px}

/* process */
.step-title{font-family:"Rubik",sans-serif;font-size:17px;color:var(--ink);text-align:center;width:270px}
.step-copy{font-size:12.5px;line-height:22px;color:var(--muted);text-align:center;width:270px}

/* press */
.press{left:157px;top:1578px;width:1043px;height:149px;background:var(--panel)}
.press .names{left:45px;top:0;height:149px;display:flex;align-items:center;gap:58px;font-family:"Rubik",sans-serif;font-weight:500;font-size:22px;color:#3c3f46}

/* schedule */
.event{left:157px;width:886px;height:191px;background:var(--white)}
.event.raised{box-shadow:0 4px 26px rgba(30,35,45,.09)}
.event .num{left:37px;top:52px;font-family:"Rubik",sans-serif;font-weight:300;font-size:70px;color:var(--gold);line-height:1}
.event .date{left:138px;top:82px;font-size:14px;line-height:19px;color:var(--muted)}
.event .thumb{left:248px;top:30px;width:135px;height:126px;border-radius:6px}
.event h4{left:410px;top:42px;font-family:"Rubik",sans-serif;font-weight:500;font-size:17px;color:var(--ink)}
.event p{left:410px;top:76px;width:460px;font-size:12px;line-height:22px;color:var(--muted)}
.event .more{left:410px;top:136px;font-size:12px;font-weight:600;color:var(--ink)}

/* solutions */
.solutions{left:0;top:2350px;width:1200px;height:466px;background:linear-gradient(180deg,#c9a43f 0%,#9f7a52 30%,#7a4c62 62%,#5e3e6b 100%);overflow:hidden}

/* blog cards */
.post{top:3444px;width:278px;height:374px;background:var(--white);box-shadow:0 4px 24px rgba(30,35,45,.08)}
.post .img{left:0;top:0;width:278px;height:174px}
.post .badge{right:0;top:120px;width:80px;height:54px;background:var(--gold);color:var(--white);font-family:"Rubik",sans-serif;font-weight:500;font-size:17px;text-align:center;line-height:22px;padding-top:6px}
.post h5{left:24px;top:198px;width:235px;font-family:"Rubik",sans-serif;font-weight:500;font-size:14.5px;line-height:20px;color:var(--ink)}
.post p{left:24px;top:250px;width:230px;font-size:12px;line-height:21px;color:var(--muted)}
.post .more{left:24px;top:324px;font-size:12.5px;font-weight:600;color:var(--ink)}

/* footer */
.footer{left:0;top:3899px;width:1200px;height:394px;background:var(--ink);color:var(--white)}
.footer .brand{top:75px;font-size:23px}
.footer h6{font-family:"Rubik",sans-serif;font-weight:500;font-size:16px;top:146px}
.footer ul{list-style:none;top:192px;font-size:13px;line-height:29px}
.footer .field{left:771px;top:198px;width:228px;height:37px;background:var(--white);border-radius:3px;color:#b8bbc1;font-size:10px;padding:12px 12px}
.footer .subscribe{left:771px;top:247px;width:115px;height:37px;border-radius:3px;line-height:37px;font-size:13px}
.footer .circles{left:771px;top:303px;display:flex;gap:10px}
.footer .circles span{width:22px;height:22px;border-radius:50%;background:var(--white);display:block}
.legal{left:0;top:4293px;width:1200px;height:52px;background:var(--ink-deep);color:#c9ccd2;font-size:10px;text-align:center;line-height:52px}
</style>
</head>
<body>

<header class="abs topbar">
  <span class="abs tagline">Helping Create Success</span>
  <span class="abs phone">+1.800.555.0142</span>
  <span class="abs mailbox">Email@example.com</span>
  <div class="abs socials"><span></span><span></span><span></span><span></span></div>
</header>

<nav class="abs nav">
  <a class="abs brand" href="#">Corinne Valbeck</a>
  <div class="abs menu">
    <a class="active" href="#">Home</a><a href="#">About</a><a href="#">Videos &amp; Topics</a><a href="#">Events Books</a><a href="#">The Nest Podcast</a><a href="#">Contact</a>
  </div>
  <a class="abs cta" href="#">REQUEST A QUOUTE</a>
</nav>

<section class="abs hero">
  <div class="abs photo" role="img" aria-label="Black and white portrait of Corinne reaching toward the camera"></div>
  <h1 class="abs">Wisdom Begins<br>with Wonder.</h1>
  <p class="abs">Lorem ipsum dolor sit amet, consectetur adipiscing elit, sed do eiusmod tempor incididunt ut labore et dolore magna aliqua. Ut enim ad minim veniam</p>
  <a class="abs btn" href="#">View More</a>
  <div class="abs feature blog">
    <span class="ico"><svg width="28" height="28" viewBox="0 0 28 28" fill="none" stroke="#fff" stroke-width="1.8"><rect x="5" y="4" width="16" height="20" rx="2"/><path d="M9 10h8M9 14h8M9 18h5"/></svg></span>
    <div><h3>Visit My Blog</h3><em>Sed ut perspiciatis unde om natus er sit volup</em></div>
  </div>
  <div class="abs feature videos">
    <span class="ico"><svg width="28" height="28" viewBox="0 0 28 28" fill="none" stroke="#d4ad3f" stroke-width="1.8"><rect x="4" y="6" width="20" height="14" rx="2"/><path d="M12 10v6l5-3z" fill="#d4ad3f"/><path d="M10 23h8"/></svg></span>
    <div><h3>View Our Videos</h3><em>Sed ut perspiciatis unde om natus er sit volup</em></div>
  </div>
</section>

<!-- about -->
<span class="abs ghost" style="left:158px;top:675px">About</span>
<h2 class="abs sec-title" style="left:155px;top:717px;width:420px">Sed ut perspiciatis unde omnis iste nat</h2>
<p class="abs copy" style="left:157px;top:818px;width:415px">Lorem ipsum dolor sit amet, consectetur adipiscing elit, sed do eiusmod tempor incididunt ut labore et dolore magna aliqua. Ut enim ad minim veniam, quis nostrud exercitation ullamco laboris nisi ut aliquip exea commodo consequat.</p>
<p class="abs copy" style="left:157px;top:932px;width:415px">Duis aute irure dolor in reprehenderit in voluptate velit esse cillum dolore eu fugiat nulla pariatur</p>
<a class="abs btn" href="#" style="left:157px;top:1009px;width:142px;height:41px">View More</a>
<div class="abs tablet" style="left:614px;top:733px;width:425px;height:295px">
  <div class="screen" role="img" aria-label="Video still of Corinne with arms raised above a red rock canyon" style="background:linear-gradient(180deg,#6f9ad0 0%,#a9c3df 30%,#c07a4d 55%,#9c5a38 100%)"></div>
  <svg class="abs playmark" viewBox="0 0 44 44"><circle cx="22" cy="22" r="19" fill="rgba(255,255,255,.2)" stroke="#fff" stroke-width="2"/><path d="M18 14v16l12-8z" fill="#fff"/></svg>
</div>

<!-- process -->
<div class="abs center" style="top:1098px"><span class="ghost">Process</span></div>
<h2 class="abs sec-title center" style="top:1134px">Neque porro quisquam est</h2>
<svg class="abs" style="left:150px;top:1228px" width="900" height="280" viewBox="0 0 900 280">
  <path d="M7 136h750l8 8-8 8H7l8-8z" fill="#d4ad3f"/>
  <path d="M220 138l6 6-6 6M480 138l6 6-6 6M742 138l6 6-6 6" fill="none" stroke="#fff" stroke-width="2"/>
  <g fill="#d4ad3f">
    <line x1="120" y1="100" x2="120" y2="136" stroke="#d4ad3f" stroke-width="3"/>
    <circle cx="120" cy="60" r="40"/>
    <line x1="560" y1="100" x2="560" y2="136" stroke="#d4ad3f" stroke-width="3"/>
    <circle cx="560" cy="60" r="40"/>
    <line x1="340" y1="152" x2="340" y2="190" stroke="#d4ad3f" stroke-width="3"/>
    <circle cx="340" cy="229" r="40"/>
    <line x1="780" y1="152" x2="780" y2="190" stroke="#d4ad3f" stroke-width="3"/>
    <circle cx="780" cy="229" r="40"/>
  </g>
  <g fill="none" stroke="#fff" stroke-width="2">
    <circle cx="120" cy="60" r="20"/><path d="M110 50l20 20M130 50l-20 20"/>
    <path d="M548 50l12-8 12 8v18h-24z"/><path d="M554 60h12"/>
    <circle cx="340" cy="229" r="8"/><circle cx="326" cy="242" r="5"/><circle cx="354" cy="242" r="5"/><path d="M340 212v9"/>
    <circle cx="780" cy="222" r="9"/><path d="M764 244h32M770 244v-6h20v6"/>
  </g>
</svg>
<div class="abs step-title" style="left:355px;top:1244px">Sed ut perspiciatis</div>
<div class="abs step-copy" style="left:355px;top:1276px">Neque porro quisquam est, qui dolorem ipsum quia dolor sit amet</div>
<div class="abs step-title" style="left:764px;top:1244px">Sed ut perspiciatis</div>
<div class="abs step-copy" style="left:764px;top:1276px">Neque porro quisquam est, qui dolorem ipsum quia dolor sit amet</div>
<div class="abs step-title" style="left:160px;top:1413px">Sed ut perspiciatis</div>
<div class="abs step-copy" style="left:160px;top:1445px">Neque porro quisquam est, qui dolorem ipsum quia dolor sit amet</div>
<div class="abs step-title" style="left:579px;top:1413px">Sed ut perspiciatis</div>
<div class="abs step-copy" style="left:579px;top:1445px">Neque porro quisquam est, qui dolorem ipsum quia dolor sit amet</div>

<!-- press -->
<div class="abs press">
  <div class="abs names"><span>Quillpost</span><span>Northgate Review</span><span>The Ledger</span><span>The Courier</span><span>The Dispatch</span></div>
</div>

<!-- schedule -->
<div class="abs center" style="top:1788px"><span class="ghost">Schedule</span></div>
<h2 class="abs sec-title center" style="top:1826px">Sed ut perspiciatis unde omn</h2>
<article class="abs event raised" style="top:1911px">
  <span class="abs num">01</span>
  <span class="abs date">December<br>WEDNESDAY</span>
  <div class="abs thumb" role="img" aria-label="Corinne beside a wall of brand stickers" style="background:linear-gradient(135deg,#d9c59a,#6d7a52 60%,#e8e3d8)"></div>
  <h4 class="abs">Sed ut perspiciatis unde</h4>
  <p class="abs">Omnis iste natus error sit volup tatem accusantium dolorem que laudantium, totam rem aperiam, eaque ipsa quae ab illo iantium.</p>
  <span class="abs more">Learn More...</span>
</article>
<article class="abs event" style="top:2104px">
  <span class="abs num">22</span>
  <span class="abs date">December<br>WEDNESDAY</span>
  <div class="abs thumb" role="img" aria-label="Corinne in a wide-brim hat looking over a desert valley" style="background:linear-gradient(180deg,#5e86b8 0%,#a9bfd6 45%,#8a7a66 100%)"></div>
  <h4 class="abs">Sed ut perspiciatis unde</h4>
  <p class="abs">Omnis iste natus error sit volup tatem accusantium dolorem que laudantium, totam rem aperiam, eaque ipsa quae ab illo iantium.</p>
  <span class="abs more">Learn More...</span>
</article>

<!-- solutions -->
<section class="abs solutions" role="img" aria-label="Blurred event photo of Corinne with fellow speakers on stage">
  <div class="abs center" style="top:62px"><span class="ghost" style="color:rgba(255,255,255,.16)">Solutions</span></div>
  <h2 class="abs sec-title center" style="top:103px;color:#fff">Neque porro quisquam est</h2>
  <p class="abs" style="left:195px;top:175px;width:810px;text-align:center;font-size:12.5px;line-height:23px;color:#fff">Lorem ipsum dolor sit amet, consectetur adipiscing elit, sed do eiusmod tempor incididunt ut labore et dolore magna aliqua. Ut enim ad minim veniam, quis nostrud exercitation ullamco laboris nisi ut aliquip exea commodo consequat. Duis aute irure dolor in reprehenderit in voluptate velit esse cillum dolore eu fugiat</p>
  <svg class="abs" style="left:568px;top:265px" width="64" height="64" viewBox="0 0 64 64"><circle cx="32" cy="32" r="29" fill="none" stroke="#fff" stroke-width="3"/><path d="M26 20v24l18-12z" fill="#fff"/></svg>
</section>

<!-- about corinne -->
<div class="abs tablet" style="left:159px;top:2907px;width:425px;height:329px">
  <div class="screen" role="img" aria-label="Video still of Corinne presenting beside a poster of the earth" style="background:linear-gradient(90deg,#2c3a4a 0%,#4a5b6d 55%,#b25a35 70%,#7a4a32 100%)"></div>
  <svg class="abs playmark" viewBox="0 0 44 44"><circle cx="22" cy="22" r="19" fill="rgba(255,255,255,.2)" stroke="#fff" stroke-width="2"/><path d="M18 14v16l12-8z" fill="#fff"/></svg>
</div>
<span class="abs ghost" style="left:634px;top:2898px">About</span>
<h2 class="abs sec-title" style="left:631px;top:2933px">Corinne Valbeck</h2>
<p class="abs copy" style="left:631px;top:2994px;width:415px">Lorem ipsum dolor sit amet, consectetur adipiscing elit, sed do eiusmod tempor incididunt ut labore et dolore magna aliqua. Ut enim ad minim veniam, quis nostrud exercitation ullamco laboris nisi ut aliquip exea commodo consequat.</p>
<p class="abs copy" style="left:631px;top:3108px;width:415px">Duis aute irure dolor in reprehenderit in voluptate velit esse cillum dolore eu fugiat nulla pariatur</p>
<a class="abs btn" href="#" style="left:633px;top:3187px;width:140px;height:41px">View More</a>

<!-- blog -->
<div class="abs center" style="top:3322px"><span class="ghost">Blog</span></div>
<h2 class="abs sec-title center" style="top:3362px">Sed ut perspiciatis unde</h2>
<article class="abs post" style="left:152px">
  <div class="abs img" role="img" aria-label="Black and white photo of Corinne with a horse" style="background:linear-gradient(135deg,#cfcfcf,#5a5a5a 60%,#2b2b2b)"></div>
  <div class="abs badge">AUG<br>13</div>
  <h5 class="abs">Sunt in culpa qui officia dese nt mollit anim id est</h5>
  <p class="abs">Lorem Ipsum is simply dummy of the printing and typeset ting in dustry Lorem Ipsum</p>
  <span class="abs more">Learn More</span>
</article>
<article class="abs post" style="left:461px">
  <div class="abs img" role="img" aria-label="Pale blue two-storey house under a clear sky" style="background:linear-gradient(180deg,#4f8fd6 0%,#9fc0e3 35%,#d7dee6 60%,#5f8a48 100%)"></div>
  <div class="abs badge">AUG<br>13</div>
  <h5 class="abs">Sunt in culpa qui officia dese nt mollit anim id est</h5>
  <p class="abs">Lorem Ipsum is simply dummy of the printing and typeset ting in dustry Lorem Ipsum</p>
  <span class="abs more">Learn More</span>
</article>
<article class="abs post" style="left:771px">
  <div class="abs img" role="img" aria-label="Child feeding horses at a wooden fence" style="background:linear-gradient(135deg,#b9a58a,#7a5a3e 55%,#d3a9b3)"></div>
  <div class="abs badge">AUG<br>13</div>
  <h5 class="abs">Sunt in culpa qui officia dese nt mollit anim id est</h5>
  <p class="abs">Lorem Ipsum is simply dummy of the printing and typeset ting in dustry Lorem Ipsum</p>
  <span class="abs more">Learn More</span>
</article>

<!-- footer -->
<footer class="abs footer">
  <div class="abs brand center">Corinne Valbeck</div>
  <h6 class="abs" style="left:250px">Our Links</h6>
  <ul class="abs" style="left:250px"><li>Home</li><li>About</li><li>Videos &amp; Topics</li><li>Events Books</li><li>Contact</li></ul>
  <h6 class="abs" style="left:495px">Workshops</h6>
  <ul class="abs" style="left:495px"><li>Design Sprints Done Right</li><li>Get started with Wireloom</li><li>Wireframe in a Day</li><li>Using Jobs-to-be-Done for</li><li>Better Product Strategy</li></ul>
  <h6 class="abs" style="left:771px">Newsletter Subscribe</h6>
  <div class="abs field">Email Adresss</div>
  <a class="abs btn subscribe" href="#">Subscribe</a>
  <div class="abs circles"><span></span><span></span><span></span></div>
</footer>
<div class="abs legal">© Copyright Corinne Valbeck All rights reserved.</div>

</body>
</html>
```